Primary Home Page Graphic: Crowdfund and Non-Profit Social Promotion Website

WHAT WE NEED: See attached. I need a graphic designed that is comparable to these. The graphic will replace the home page video on our current website Kelvanox.com
PREFERRED LOOK: Much like attached. Black/white with color that pops. Must have crowdfunding/non-profit + social media appearance.
WHAT WE DO: Social Promotion of Crowdfunding and Non-Profit Campaigns > the image you design should reflect this subject content.
TEXT ON GRAPHIC:
Your Campaign, Shared.
Get your message moving across social media within minutes.
Thousands of social voices are on stand-by and ready to assist.
Project Deadline Extended
Reason: Not seeing the perfect fit yet for the page. Want to see if we can get some other ideas. Looking for black and white image with title and text displayed in a modern way.
The main graphic needs to appear such as Crowdfunding. Keep the text the same with a call to action.
Please use close attention to detail, modern design technique and good contrast on the colors. Thanks.

```html
<!DOCTYPE html>
<html lang="en">
<head>
<meta charset="utf-8">
<title>Kelvanox – Your Campaign Shared</title>
<link rel="stylesheet" href="https://fonts.googleapis.com/css2?family=Michroma&family=Open+Sans:wght@400;600&display=swap">
<style>
  :root {
    --backdrop-dark: #1c1c1c;
    --backdrop-mid: #4a4a4a;
    --backdrop-light: #6e6e6e;
    --bubble-orange: #e2620f;
    --ink-white: #ffffff;
    --rule-dots: rgba(255, 255, 255, 0.55);
    --button-ink: #3a3a3a;
  }
  * { margin: 0; padding: 0; box-sizing: border-box; }
  html, body {
    width: 1200px;
    height: 588px;
    overflow: hidden;
    background: var(--backdrop-dark);
  }
  .hero {
    position: relative;
    width: 1200px;
    height: 588px;
    overflow: hidden;
  }
  .hero-backdrop {
    position: absolute;
    inset: 0;
    background:
      radial-gradient(ellipse 60% 70% at 62% 40%, var(--backdrop-light) 0%, var(--backdrop-mid) 45%, var(--backdrop-dark) 100%);
  }
  .speech-bubble {
    position: absolute;
    left: 0;
    top: 0;
    width: 1200px;
    height: 588px;
  }
  .bubble-content {
    position: absolute;
    left: 380px;
    top: 0;
    width: 440px;
    text-align: center;
    color: var(--ink-white);
  }
  .brand-mark {
    position: absolute;
    top: 128px;
    left: 0;
    width: 100%;
    display: flex;
    align-items: center;
    justify-content: center;
    gap: 10px;
    font-family: "Open Sans", sans-serif;
    font-weight: 600;
    font-size: 26px;
    color: var(--ink-white);
  }
  .brand-dot {
    width: 14px;
    height: 14px;
    border-radius: 50%;
    background: var(--ink-white);
  }
  .eyebrow {
    position: absolute;
    top: 220px;
    left: 0;
    width: 100%;
    font-family: "Michroma", sans-serif;
    font-size: 19px;
    letter-spacing: 0.5px;
    line-height: 24px;
  }
  .title-rule {
    position: absolute;
    left: 75px;
    width: 290px;
    border-top: 1px dotted var(--rule-dots);
  }
  .title-rule.top { top: 251px; }
  .title-rule.bottom { top: 304px; }
  .headline {
    position: absolute;
    top: 252px;
    left: 0;
    width: 100%;
    font-family: "Michroma", sans-serif;
    font-size: 44px;
    line-height: 52px;
    letter-spacing: 1px;
  }
  .lead {
    position: absolute;
    top: 315px;
    left: 0;
    width: 100%;
    font-family: "Open Sans", sans-serif;
    font-size: 14px;
    line-height: 20px;
  }
  .sublead {
    position: absolute;
    top: 336px;
    left: 0;
    width: 100%;
    font-family: "Open Sans", sans-serif;
    font-size: 12.5px;
    line-height: 18px;
  }
  .cta-button {
    position: absolute;
    top: 382px;
    left: 146px;
    width: 147px;
    height: 51px;
    background: var(--ink-white);
    border-radius: 3px;
    color: var(--button-ink);
    font-family: "Open Sans", sans-serif;
    font-size: 12px;
    line-height: 51px;
    text-decoration: none;
    display: block;
  }
</style>
</head>
<body>
  <main class="hero">
    <div class="hero-backdrop" role="img" aria-label="Black and white close-up photograph of a computer keyboard with a crowdfunding key"></div>

    <svg class="speech-bubble" viewBox="0 0 1200 588" aria-hidden="true">
      <path fill="var(--bubble-orange)" fill-opacity="0.94"
        d="M600 84
           A220 220 0 0 1 628 522
           Q606 520 601 532
           Q596 520 572 522
           A220 220 0 0 1 600 84 Z"/>
    </svg>

    <section class="bubble-content">
      <div class="brand-mark"><span class="brand-dot"></span>Kelvanox</div>
      <p class="eyebrow">YOUR CAMPAIGN</p>
      <span class="title-rule top"></span>
      <h1 class="headline">SHARED</h1>
      <span class="title-rule bottom"></span>
      <p class="lead">Get your message moving across social media within minutes.</p>
      <p class="sublead">Thousands of social voices are on stand-by and ready to assist.</p>
      <a class="cta-button" href="#">LET'S GET STARTED</a>
    </section>
  </main>
</body>
</html>
```